Corporate Branding - Web and Print

A UK based company will like to use an existing logo to create branding materials for all marketing related documents, including business card, prints, letterhead, Website, Twitter, Facebook, Instagram logo etc. This company serves high-end clientele in the fashion, health and wellness and as such high quality and class is of utmost importance.
Where the logo can be modernised without losing its character then experiment. The main thing is to have a corporate branding which can be used later for brochures, Business Plan infographics.
The prominent colour within the organisation is burnt orange with no secondary colour. However if you believe a secondary colour is needed then use it, otherwise keep it simple and classy. Any chosen colours have to match perfectly.
Target Market(s)
High net worth individuals
Industry/Entity Type
Health And Wellness
Contact Information for Business Card
classy
Look and feel
Each slider illustrates characteristics of the customer's brand and the style your logo design should communicate.

```html
<!DOCTYPE html>
<html lang="en">
<head>
<meta charset="UTF-8">
<title>Velura Business Card</title>
<link href="https://fonts.googleapis.com/css2?family=Roboto:wght@400;500;900&display=swap" rel="stylesheet">
<style>
  :root {
    --brand-orange: #f7941d;
    --card-white: #ffffff;
    --text-grey: #444444;
    --divider: #b0553a;
    --page-bg: #ecebe8;
  }
  * { margin: 0; padding: 0; box-sizing: border-box; }
  html, body {
    width: 1200px; height: 1200px; overflow: hidden;
    background: var(--page-bg);
    font-family: "Roboto", Arial, sans-serif;
  }
  .canvas {
    width: 1200px; height: 1200px;
    display: flex; flex-direction: column; align-items: center; justify-content: center;
    gap: 45px;
  }
  .card {
    width: 800px; height: 455px;
    border-radius: 20px;
    position: relative;
    overflow: hidden;
    box-shadow: 0 4px 14px rgba(0,0,0,0.18);
  }
  .card-front { background: var(--card-white); }
  .card-back { background: var(--brand-orange); }

  .brand-lockup {
    position: absolute;
    display: flex; flex-direction: column; align-items: center;
  }
  .card-front .brand-lockup { left: 60px; top: 160px; width: 300px; }
  .brand-dot { border-radius: 50%; }
  .card-front .brand-dot { width: 80px; height: 80px; background: var(--brand-orange); margin-bottom: 12px; }
  .brand-name {
    font-weight: 900; letter-spacing: 2px; line-height: 1;
  }
  .card-front .brand-name { font-size: 50px; color: var(--brand-orange); }

  .divider {
    position: absolute; left: 401px; top: 104px;
    width: 1.5px; height: 246px; background: var(--divider);
  }
  .contact-block {
    position: absolute; left: 438px; top: 96px;
    color: var(--text-grey);
  }
  .person-name { font-size: 31px; font-weight: 500; color: var(--brand-orange); line-height: 1.1; }
  .person-title { font-size: 21px; margin-top: 4px; }
  .address { font-size: 20px; line-height: 27px; margin-top: 22px; }
  .contact-list { list-style: none; margin-top: 18px; }
  .contact-list li {
    display: flex; align-items: center; gap: 8px;
    font-size: 20px; line-height: 28.5px;
  }
  .contact-icon { width: 18px; height: 18px; flex: none; }

  .card-back .brand-lockup { left: 0; right: 0; top: 118px; }
  .card-back .brand-dot { width: 118px; height: 118px; background: var(--card-white); margin-bottom: 22px; }
  .card-back .brand-name { font-size: 72px; color: var(--card-white); letter-spacing: 3px; }
</style>
</head>
<body>
<main class="canvas">
  <section class="card card-front">
    <div class="brand-lockup">
      <div class="brand-dot"></div>
      <div class="brand-name">VELURA</div>
    </div>
    <div class="divider"></div>
    <div class="contact-block">
      <h1 class="person-name">Adrian Hale</h1>
      <p class="person-title">President &amp; CEO</p>
      <p class="address">220 Marlow Road, Suite 14<br>Kingsford Hill, CA 3050</p>
      <ul class="contact-list">
        <li>
          <svg class="contact-icon" viewBox="0 0 24 24" fill="none" stroke="#f7941d" stroke-width="1.8" stroke-linejoin="round"><path d="M5 3h4l2 5-2.5 1.5a11 11 0 0 0 6 6L16 13l5 2v4a2 2 0 0 1-2 2A16 16 0 0 1 3 5a2 2 0 0 1 2-2z"/></svg>
          000-000-0000
        </li>
        <li>
          <svg class="contact-icon" viewBox="0 0 24 24" fill="none" stroke="#f7941d" stroke-width="1.8"><rect x="6" y="2" width="12" height="20" rx="2"/><line x1="11" y1="18" x2="13" y2="18"/></svg>
          000-000-0000
        </li>
        <li>
          <svg class="contact-icon" viewBox="0 0 24 24" fill="none" stroke="#f7941d" stroke-width="1.8"><rect x="2" y="5" width="20" height="14"/><path d="M2 5l10 8 10-8M2 19l7-7M22 19l-7-7"/></svg>
          a.hale@velura-studio.com
        </li>
        <li>
          <svg class="contact-icon" viewBox="0 0 24 24" fill="none" stroke="#f7941d" stroke-width="1.8"><circle cx="12" cy="12" r="10"/><ellipse cx="12" cy="12" rx="4" ry="10"/><line x1="2" y1="12" x2="22" y2="12"/><path d="M4 7h16M4 17h16"/></svg>
          www.velura-studio.com
        </li>
      </ul>
    </div>
  </section>

  <section class="card card-back">
    <div class="brand-lockup">
      <div class="brand-dot"></div>
      <div class="brand-name">VELURA</div>
    </div>
  </section>
</main>
</body>
</html>
```